Hearth Twisters Grand Opening 2-for-1 Sale Postcard Design

Who we are: Hearth Twisters will come to you. We roll your medical marijuana in the privacy and safety of your home. We roll your medicine for you.

We need a postcard design that meets NPDS RCTZ requirements for our Grand Opening 2-for-1 Sale. Please include some or all of our logo.
Looking for elegant, upscale design. Appeal to luxury buyers with more money than time.
Updates

2-for-1 offer good thru March 31, 2015.Please add a small recycle image to convey the fact that we recycle. Added Tuesday, December 8, 2015

Target Market(s)

Income $50K+, Age 35+, College education, Left politically, No kids or older kids

Industry/Entity Type

Health Service

Requirements
Must have
• Our logo
• Our contact number: (574) 218-3065
• NPDS Postcard/RCTZ comptability layout on back of card.
• 2-for-1 Offer good thru March 31st, 2016.
Nice to have
• 2-3 colors, white text on dark green background
Should not have
• Images of marijuana. Please limit marijuana images to our logo.

```html
<!DOCTYPE html>
<html lang="en">
<head>
<meta charset="utf-8">
<title>Hearth Twisters Grand Opening Postcard</title>
<link href="https://fonts.googleapis.com/css2?family=Oswald:wght@500;600;700&family=Open+Sans:wght@600;700&display=swap" rel="stylesheet">
<style>
  :root {
    --page: #e4e4e4;
    --white: #ffffff;
    --green-deep: #16421a;
    --green-mid: #2f7a2c;
    --green-glow: #4fae3c;
    --green-bright: #5cc247;
    --brand-green: #2f6b2a;
    --yellow: #ffe81a;
    --ribbon-light: #f4ec3c;
    --ribbon-dark: #b8ae12;
    --ribbon-text: #1f3b1c;
    --ink: #222222;
  }
  * { margin: 0; padding: 0; box-sizing: border-box; }
  html, body { width: 975px; height: 1200px; overflow: hidden; }
  body { background: var(--page); position: relative; font-family: "Open Sans", Arial, sans-serif; }

  .postcard { position: absolute; left: 129px; width: 705px; height: 543px; background: var(--white); overflow: hidden; }
  .postcard--front { top: 47px; }
  .postcard--back { top: 616px; }
  .postcard__shapes { position: absolute; inset: 0; width: 100%; height: 100%; }

  .brand { position: absolute; display: flex; align-items: center; gap: 8px;
    font-family: "Open Sans", Arial, sans-serif; font-weight: 700; font-size: 28px;
    color: var(--brand-green); line-height: 1; letter-spacing: -0.5px; z-index: 2; }
  .brand__mark { width: 14px; height: 14px; background: var(--brand-green); }
  .postcard--front .brand { left: 33px; top: 84px; }
  .postcard--back .brand { left: 20px; top: 80px; font-size: 27px; }

  .text { position: absolute; line-height: 1; white-space: nowrap; }
  .condensed { font-family: "Oswald", "Arial Narrow", sans-serif; }
  .sans { font-family: "Open Sans", Arial, sans-serif; }
  .is-white { color: var(--white); }
  .is-yellow { color: var(--yellow); }
  .centered { left: 0; width: 100%; text-align: center; }

  .ribbon__title { position: absolute; left: 104px; width: 494px; top: 170px; text-align: center;
    font-family: "Oswald", "Arial Narrow", sans-serif; font-weight: 700; font-size: 50px;
    color: var(--ribbon-text); line-height: 1; transform: rotate(2deg); letter-spacing: 1px; }

  .opening-month { top: 262px; font-weight: 700; font-size: 22px; }
  .book-front { top: 288px; font-weight: 600; font-size: 36px; }
  .phone-front { top: 323px; font-weight: 600; font-size: 52px; }

  .offer-date { left: 14px; width: 300px; text-align: center; top: 418px; font-weight: 700; font-size: 24px; }
  .offer-title { left: 14px; width: 300px; text-align: center; top: 449px; font-weight: 700; font-size: 33px; }
  .added-day { left: 400px; width: 285px; text-align: center; top: 421px; font-weight: 700; font-size: 25px; }
  .added-date { left: 400px; width: 285px; text-align: center; top: 450px; font-weight: 700; font-size: 28px; }

  .recycle-badge { position: absolute; left: 300px; top: 408px; width: 104px; height: 100px; border-radius: 50%;
    background: radial-gradient(circle, #e2dc5a 0%, #a9a326 55%, rgba(80, 110, 30, 0) 72%); }

  .tagline-top { left: 33px; top: 204px; font-weight: 600; font-size: 27px; }
  .tagline-main { left: 30px; top: 229px; font-weight: 600; font-size: 66px; }
  .tagline-bottom { left: 33px; top: 306px; font-weight: 600; font-size: 25px; letter-spacing: 7px; }
  .book-back { left: 33px; top: 378px; font-weight: 600; font-size: 36px; }
  .phone-back { left: 30px; top: 414px; font-weight: 600; font-size: 50px; }

  .stamp-box { position: absolute; left: 571px; top: 51px; width: 93px; height: 90px; border: 2px solid var(--ink); }
</style>
</head>
<body>

<section class="postcard postcard--front" aria-label="Postcard front">
  <svg class="postcard__shapes" viewBox="0 0 705 543" preserveAspectRatio="none" aria-hidden="true">
    <defs>
      <radialGradient id="front-glow" cx="0.5" cy="0.45" r="0.65">
        <stop offset="0" stop-color="#4fae3c"/>
        <stop offset="0.55" stop-color="#2f7a2c"/>
        <stop offset="1" stop-color="#16421a"/>
      </radialGradient>
      <linearGradient id="ribbon-fill" x1="0" y1="0" x2="0" y2="1">
        <stop offset="0" stop-color="#f8f25a"/>
        <stop offset="1" stop-color="#d8cf1c"/>
      </linearGradient>
    </defs>
    <rect width="705" height="543" fill="url(#front-glow)"/>
    <path d="M0 108 C70 150 150 180 220 168 C330 148 430 70 705 62 L705 0 L0 0 Z" fill="#5cc247"/>
    <path d="M0 98 C70 140 150 168 220 156 C330 138 430 60 705 50 L705 0 L0 0 Z" fill="#ffffff"/>
    <polygon points="104,195 150,180 165,250 112,266 130,230" fill="#b8ae12"/>
    <polygon points="598,210 552,195 540,262 590,282 574,246" fill="#b8ae12"/>
    <path d="M142 160 Q350 140 562 178 L552 252 Q350 214 150 234 Z" fill="url(#ribbon-fill)"/>
  </svg>

  <div class="brand"><span class="brand__mark"></span>Hearth Twisters</div>

  <div class="ribbon__title">GRAND OPENING</div>

  <div class="text centered condensed is-white opening-month">JANUARY 2015</div>
  <div class="text centered sans is-white book-front">BOOK TODAY</div>
  <div class="text centered condensed is-white phone-front">(574) 218-3065</div>

  <div class="text sans is-white offer-date">MARCH 31, 2015</div>
  <div class="text condensed is-yellow offer-title">2-FOR-1 SALE</div>

  <div class="recycle-badge" role="img" aria-label="Recycling symbol in gold"></div>

  <div class="text condensed is-white added-day">TUESDAY</div>
  <div class="text condensed is-yellow added-date">DECEMBER 8, 2015</div>
</section>

<section class="postcard postcard--back" aria-label="Postcard back">
  <svg class="postcard__shapes" viewBox="0 0 705 543" preserveAspectRatio="none" aria-hidden="true">
    <path d="M0 170 C130 170 232 152 264 112 C284 82 298 52 320 50 C342 120 397 230 420 330 C440 420 380 500 348 543 L0 543 Z" fill="#5cc247"/>
    <path d="M0 170 C130 170 232 152 264 112 C282 84 292 56 306 50 C326 120 380 230 402 330 C420 420 360 500 330 543 L0 543 Z" fill="#1f5a22"/>
  </svg>

  <div class="brand"><span class="brand__mark"></span>Hearth Twisters</div>

  <div class="text sans is-white tagline-top">WE ROLL YOUR</div>
  <div class="text condensed is-yellow tagline-main">MEDICINE</div>
  <div class="text sans is-white tagline-bottom">FOR YOU</div>

  <div class="text sans is-white book-back">BOOK TODAY</div>
  <div class="text condensed is-yellow phone-back">(574) 218-3065</div>

  <div class="stamp-box"></div>
</section>

</body>
</html>
```